Business cards

We need business cards for the logo that you designed for our company. Something simple and clean.

Target Market(s)

Homeowners/ people looking for construction work

Industry/Entity Type

Construction

Contact Information for Business Card

Name: Doug Whitby, Number: 602-555-0174, Email: WhitbyBuildingCompany@mailbox-example.net ROC# 482063

Font styles to use
Serif

Colors

Designer to choose colors to be used in the design.

Requirements
Must have
• On one side of the card I would like to be all of the personal information I have put above along with the company logo that I have attached.
• On the other side of the card I would like the top half of the card to be the logo and then on the bottom half I would like to have the areas of construction we focus on along with an icon that represents it like the picture I have attached.
• Areas we focus on:
• Roofing, Kitchen and bath Remodel, Water Damage, Storm Damage, Fire Damage, Insurance Specialist
• If we could arrange those in alphabetical order.
Nice to have
• I have added 2 company logos a colorful one and a black one it would be nice to see a couple different options the black logo to be more simple and sleek and the colorful logo to be more colorful

```html
<!DOCTYPE html>
<html lang="en">
<head>
<meta charset="utf-8">
<title>Whitby Building Company – Business Cards</title>
<link href="https://fonts.googleapis.com/css2?family=Catamaran:wght@500;600;700&family=Fjalla+One&display=swap" rel="stylesheet">
<style>
  :root {
    --page: #ffffff;
    --card: #2b3440;
    --card-inner: #27303b;
    --blue: #62a3d6;
    --red: #c9252d;
    --white: #ffffff;
  }
  html, body {
    margin: 0;
    width: 1200px;
    height: 1200px;
    overflow: hidden;
    background: var(--page);
  }
  .canvas {
    position: relative;
    width: 1200px;
    height: 1200px;
  }
  .card {
    position: absolute;
    left: 248px;
    width: 705px;
    height: 415px;
    background: var(--card);
    overflow: hidden;
    box-shadow: 0 8px 18px rgba(0,0,0,0.28);
  }
  .card--front { top: 146px; }
  .card--back { top: 622px; }

  .wordmark {
    position: absolute;
    display: flex;
    align-items: center;
    gap: 16px;
    font-family: "Catamaran", sans-serif;
    font-weight: 700;
    color: var(--blue);
    text-transform: uppercase;
    line-height: 1;
  }
  .wordmark__square {
    flex: none;
    background: var(--red);
  }
  .card--front .wordmark {
    left: 54px;
    top: 62px;
    font-size: 34px;
    letter-spacing: 1px;
  }
  .card--front .wordmark__square { width: 46px; height: 46px; }

  .name-band {
    position: absolute;
    left: 0;
    top: 204px;
    width: 467px;
    height: 58px;
    background: var(--red);
    clip-path: polygon(0 0, 430px 0, 467px 100%, 0 100%);
  }
  .name-band__name {
    position: absolute;
    left: 56px;
    top: 10px;
    margin: 0;
    font-family: "Catamaran", sans-serif;
    font-weight: 600;
    font-size: 31px;
    line-height: 38px;
    color: var(--white);
  }
  .contact {
    position: absolute;
    left: 56px;
    top: 276px;
    margin: 0;
    padding: 0;
    list-style: none;
    font-family: "Catamaran", sans-serif;
    font-weight: 500;
    font-size: 19px;
    color: var(--blue);
  }
  .contact__item {
    display: flex;
    align-items: center;
    gap: 8px;
    height: 35px;
  }
  .contact__icon { width: 14px; height: 14px; fill: var(--red); flex: none; }
  .contact__domain { color: var(--red); }

  .card--back .wordmark {
    left: 0;
    right: 0;
    top: 62px;
    justify-content: center;
    font-size: 44px;
    letter-spacing: 2px;
  }
  .card--back .wordmark__square { width: 70px; height: 70px; }

  .services-band {
    position: absolute;
    left: 0;
    top: 215px;
    width: 705px;
    height: 87px;
    background: var(--red);
  }
  .services {
    position: absolute;
    left: 0;
    top: 0;
  }
  .service-label {
    position: absolute;
    top: 322px;
    width: 110px;
    margin-left: -55px;
    text-align: center;
    font-family: "Fjalla One", sans-serif;
    font-size: 17px;
    line-height: 19px;
    color: var(--white);
  }
</style>
</head>
<body>
<main class="canvas">

  <section class="card card--front" aria-label="Business card front">
    <div class="wordmark">
      <span class="wordmark__square"></span>
      <span>Whitby Building Company</span>
    </div>
    <div class="name-band">
      <h1 class="name-band__name">Doug Whitby</h1>
    </div>
    <ul class="contact">
      <li class="contact__item">
        <svg class="contact__icon" viewBox="0 0 24 24"><path d="M6.6 10.8a15.1 15.1 0 0 0 6.6 6.6l2.2-2.2a1 1 0 0 1 1-.25 11.4 11.4 0 0 0 3.6.57 1 1 0 0 1 1 1V20a1 1 0 0 1-1 1A17 17 0 0 1 3 4a1 1 0 0 1 1-1h3.5a1 1 0 0 1 1 1c0 1.25.2 2.45.57 3.57a1 1 0 0 1-.25 1z"/></svg>
        602-555-0174
      </li>
      <li class="contact__item">
        <svg class="contact__icon" viewBox="0 0 24 24"><path d="M2 5h20v14H2z M2 5l10 8 10-8" fill="var(--red)" stroke="var(--card)" stroke-width="1.6"/></svg>
        <span>WhitbyBuildingCompany<span class="contact__domain">@mailbox-example.net</span></span>
      </li>
      <li class="contact__item">
        <svg class="contact__icon" viewBox="0 0 24 24"><path d="M12 2a7 7 0 0 0-7 7c0 5.2 7 13 7 13s7-7.8 7-13a7 7 0 0 0-7-7zm0 9.5A2.5 2.5 0 1 1 12 6.5a2.5 2.5 0 0 1 0 5z"/></svg>
        ROC# 482063
      </li>
    </ul>
  </section>

  <section class="card card--back" aria-label="Business card back">
    <div class="wordmark">
      <span class="wordmark__square"></span>
      <span>Whitby Building Company</span>
    </div>
    <div class="services-band"></div>

    <svg class="services" width="705" height="415" viewBox="0 0 705 415" aria-hidden="true">
      <defs>
        <g id="pin">
          <path d="M-42 0 A42 42 0 1 1 42 0 Q38 22 0 64 Q-38 22 -42 0z" fill="var(--blue)"/>
          <circle r="34" fill="var(--card-inner)"/>
        </g>
      </defs>

      <!-- Roofing -->
      <g transform="translate(71 252)">
        <use href="#pin"/>
        <path d="M-24 8 L0 -14 L24 8 M12 -3 V-12 H17 V2" fill="none" stroke="var(--white)" stroke-width="3.5" stroke-linejoin="round"/>
      </g>
      <!-- Kitchen & Bath -->
      <g transform="translate(182 252)">
        <use href="#pin"/>
        <g fill="none" stroke="var(--white)" stroke-width="3" stroke-linejoin="round">
          <rect x="-20" y="-6" width="40" height="22" rx="2"/>
          <rect x="-13" y="0" width="18" height="10"/>
          <path d="M-12 -16 h20 v10 h-20z"/>
          <path d="M-2 -16 v-5"/>
        </g>
        <circle cx="13" cy="5" r="2" fill="var(--white)"/>
      </g>
      <!-- Water -->
      <g transform="translate(294 252)" fill="var(--white)">
        <use href="#pin"/>
        <path d="M-6 -20 C-6 -20 -20 -2 -20 6 a14 14 0 0 0 28 0 C8 -2 -6 -20 -6 -20z"/>
        <path d="M13 -10 C13 -10 4 1 4 6 a9 9 0 0 0 18 0 C22 1 13 -10 13 -10z"/>
      </g>
      <!-- Storm -->
      <g transform="translate(406 252)" fill="var(--white)">
        <use href="#pin"/>
        <path d="M-18 6 a9 9 0 0 1 1-18 a12 12 0 0 1 23-3 a10 10 0 0 1 12 11 a6 6 0 0 1 0 10z"/>
        <path d="M-2 8 L-9 20 L-2 20 L-6 30 L6 15 L-1 15 L3 8z" fill="var(--blue)"/>
      </g>
      <!-- Fire -->
      <g transform="translate(517 252)">
        <use href="#pin"/>
        <path d="M0 -24 C6 -12 18 -6 16 8 A16 16 0 0 1 -16 8 C-16 -2 -8 -6 -6 -14 C-2 -8 -2 -4 0 -2 C2 -10 0 -18 0 -24z" fill="var(--white)"/>
        <path d="M0 4 C4 8 8 10 7 15 A7 7 0 0 1 -7 15 C-7 10 -2 8 0 4z" fill="var(--card-inner)"/>
      </g>
      <!-- Insurance -->
      <g transform="translate(629 252)">
        <use href="#pin"/>
        <path d="M0 -22 L18 -15 V-2 C18 10 10 18 0 22 C-10 18 -18 10 -18 -2 V-15z" fill="var(--white)"/>
        <path d="M0 -22 L18 -15 V-2 C18 10 10 18 0 22z" fill="var(--card-inner)" opacity="0.35"/>
      </g>
    </svg>

    <p class="service-label" style="left:71px">Roofing</p>
    <p class="service-label" style="left:182px">Kitchen<span style="color:var(--red)">&amp;</span>Bath<br>Remodel</p>
    <p class="service-label" style="left:294px">Water<br>Damage</p>
    <p class="service-label" style="left:406px">Storm<br>Damage</p>
    <p class="service-label" style="left:517px">Fire<br>Damage</p>
    <p class="service-label" style="left:629px">Insurance<br>Specialist</p>
  </section>

</main>
</body>
</html>
```